We are a church and would like a flyer for a special service that is held once a quarter to get families and friends to come out to join us. See below content and details for sizes.
Church Name: Covenant Harvest Global Fellowship
Church Logo : Attached
Title : Family and Friends Day
Subtitle: Strengthening Families - Connecting Relationships
Host: Bishop Kwame Dorlin (file attached. Don't need full body. Please crop)
Date: Sunday, 24 May
Time: 9:30 AM
Address: 2967 Marlow Lane, Suite F, Bowie MD, 20716
Phone : 240 913 2268
Website: www.chgfellowship.example
Flyer Size: Facebook size 851 x 314 pixels, Flash size 680 x 340 & Power Point size Standard

```html
<!DOCTYPE html>
<html lang="en">
<head>
<meta charset="utf-8">
<title>Family and Friends Day – Facebook Banner</title>
<link rel="stylesheet" href="https://fonts.googleapis.com/css2?family=Poiret+One&family=Roboto:wght@400&display=swap">
<style>
  :root {
    --board-bg: #e6e7e9;
    --label-ink: #3a3a3a;
    --wood-light: #d98a3a;
    --wood-mid: #a3541c;
    --wood-dark: #3e1306;
    --suit-light: #8a8580;
    --suit-dark: #3f3b38;
    --cream: #ffffff;
    --paper: #ffffff;
    --brand-blue: #24448a;
    --frame-line: #c9c9c9;
  }
  html, body {
    margin: 0;
    padding: 0;
    width: 1200px;
    height: 786px;
    overflow: hidden;
    background: var(--board-bg);
  }
  .board {
    position: relative;
    width: 1200px;
    height: 786px;
  }
  .board-label {
    position: absolute;
    top: 138px;
    left: 0;
    width: 1200px;
    text-align: center;
    margin: 0;
    font-family: "Roboto", Arial, sans-serif;
    font-weight: 400;
    font-size: 38px;
    color: var(--label-ink);
  }
  .banner {
    position: absolute;
    left: 121px;
    top: 245px;
    width: 956px;
    height: 353px;
    outline: 1px solid var(--frame-line);
  }
  .banner text {
    font-family: "Poiret One", "Josefin Sans", sans-serif;
    fill: var(--cream);
  }
  .title { font-size: 92px; }
  .title-joiner { font-size: 40px; }
  .subtitle { font-size: 27px; }
  .event-date { font-size: 22px; }
  .event-detail { font-size: 19px; }
  .contact { font-size: 17px; }
  .host-name { font-size: 16px; font-style: italic; }
  .banner .church-name { fill: var(--brand-blue); font-size: 18px; font-weight: 400; }
</style>
</head>
<body>
<main class="board">
  <p class="board-label">Facebook</p>

  <svg class="banner" viewBox="0 0 956 353" width="956" height="353" xmlns="http://www.w3.org/2000/svg">
    <defs>
      <radialGradient id="wood-glow" cx="0.5" cy="0" r="0.75" fx="0.45" fy="0">
        <stop offset="0" stop-color="var(--wood-light)"/>
        <stop offset="0.45" stop-color="var(--wood-mid)"/>
        <stop offset="1" stop-color="var(--wood-dark)"/>
      </radialGradient>
      <linearGradient id="suit-tone" x1="0" y1="0" x2="1" y2="1">
        <stop offset="0" stop-color="var(--suit-light)"/>
        <stop offset="1" stop-color="var(--suit-dark)"/>
      </linearGradient>
    </defs>

    <rect class="wood-backdrop" x="0" y="0" width="956" height="353" fill="url(#wood-glow)"
          role="img" aria-label="Warm wooden plank wall backdrop"/>

    <path class="corner-sweep" d="M409 353 C 620 320, 860 240, 956 143 L956 353 Z" fill="var(--paper)"/>

    <path class="host-photo" d="M0 140 C 60 100, 180 80, 284 150 L 284 353 L 0 353 Z" fill="url(#suit-tone)"
          role="img" aria-label="Portrait of Bishop Kwame Dorlin, smiling, in a grey jacket and peach shirt"/>

    <text class="title" x="253" y="88">Friend</text>
    <text class="title-joiner" x="463" y="100">and</text>
    <text class="title" x="290" y="171">Familes</text>

    <text class="subtitle" x="285" y="215">Strengthening Families</text>
    <text class="subtitle" x="285" y="247">Connecting Relationships</text>

    <text class="host-name" x="288" y="335">Bishop Kwame Dorlin</text>

    <g class="event-info" text-anchor="end">
      <text class="event-date" x="908" y="44">Sunday, 24th May</text>
      <text class="event-detail" x="908" y="72">9:30 AM</text>
      <text class="event-detail" x="908" y="96">2967 Marlow Lane</text>
      <text class="event-detail" x="908" y="119">Suite F, Bowie MD, 20716</text>
    </g>

    <text class="contact" x="700" y="172">Phone 240 913 2268</text>
    <text class="contact" x="682" y="189">www.chgfellowship.example</text>

    <g class="church-mark" text-anchor="middle">
      <text class="church-name" x="842" y="298">Covenant Harvest</text>
      <text class="church-name" x="842" y="320">Global Fellowship</text>
    </g>
  </svg>
</main>
</body>
</html>
```